KESTRA Communications Business Card- Olde

Kestra Integrated Communications is Corporate communications agency with more than 20 years of experience. We become part of the manegement team of our clients in other to improve their outcomes and grow the possitioning of their brand.
We are in Puerto Rico, latin caribbean island
Name: Marisolde (Olde) Fuentes
787-555-0148
ofuentes@kestrakom.example

Target Market(s)

finance and pharmaceutical companies

Industry/Entity Type

Business

Contact Information for Business Card

modern, edgy colorful and playfull like our logo

Requirements
Must have
• company logo
• name
• tel
• email

```html
<!DOCTYPE html>
<html lang="en">
<head>
<meta charset="utf-8">
<title>Quelvario Communications – Business Card</title>
<link rel="stylesheet" href="https://fonts.googleapis.com/css2?family=Open+Sans:ital,wght@0,400;0,600;0,700;1,400&display=swap">
<style>
  :root {
    --page-bg: #9c9d9d;
    --card-white: #f4f4f2;
    --brand-orange: #cf501d;
    --brand-brown: #3b2a12;
    --text-dark: #3d3d3d;
    --rule-grey: #6e6e6e;
    --back-text: #f3ece6;
  }
  * { margin: 0; padding: 0; box-sizing: border-box; }
  html, body {
    width: 1105px;
    height: 1200px;
    overflow: hidden;
    background: var(--page-bg);
    font-family: "Open Sans", Arial, sans-serif;
  }
  .card {
    position: absolute;
    left: 182px;
    width: 746px;
    height: 427px;
  }
  .card-front { top: 119px; background: var(--card-white); }
  .card-back { top: 637px; height: 425px; background: var(--brand-orange); }

  /* brand name */
  .brand {
    position: absolute;
    display: flex;
    align-items: center;
    gap: 12px;
    font-weight: 700;
    letter-spacing: 1px;
    line-height: 1;
  }
  .brand-dot { border-radius: 50%; flex: none; }
  .card-front .brand {
    right: 44px;
    top: 100px;
    font-size: 42px;
    color: var(--brand-brown);
  }
  .card-front .brand-dot { width: 20px; height: 20px; background: var(--brand-orange); }
  .card-back .brand {
    left: 0; right: 0;
    justify-content: center;
    top: 185px;
    font-size: 64px;
    color: var(--brand-brown);
  }
  .card-back .brand-dot { width: 30px; height: 30px; background: var(--back-text); }

  /* identity */
  .person-name {
    position: absolute;
    left: 38px;
    top: 224px;
    font-size: 25px;
    font-weight: 600;
    line-height: 1.2;
    color: var(--brand-orange);
  }
  .person-role {
    position: absolute;
    left: 38px;
    right: 44px;
    top: 261px;
    display: flex;
    align-items: flex-end;
    gap: 4px;
    font-size: 19px;
    color: var(--text-dark);
  }
  .person-role::after {
    content: "";
    flex: 1;
    border-bottom: 1.5px solid var(--rule-grey);
    margin-bottom: 6px;
  }

  /* contacts */
  .contact-list {
    position: absolute;
    left: 40px;
    top: 302px;
    list-style: none;
  }
  .contact-item {
    display: flex;
    align-items: center;
    gap: 10px;
    height: 28.5px;
    font-size: 19px;
    color: var(--text-dark);
  }
  .contact-icon { width: 18px; height: 18px; flex: none; fill: var(--brand-orange); }

  .location {
    position: absolute;
    right: 44px;
    top: 334px;
    text-align: right;
    font-size: 19px;
    font-style: normal;
    line-height: 27px;
    color: var(--text-dark);
  }

  .front-trim {
    position: absolute;
    left: 0; right: 0; bottom: 0;
    height: 20px;
  }
  .front-trim .trim-line {
    position: absolute; left: 0; right: 0; top: 0;
    height: 3px; background: var(--brand-brown);
  }
  .front-trim .trim-band {
    position: absolute; left: 0; right: 0; bottom: 0;
    height: 13px; background: var(--brand-orange);
  }

  .back-url {
    position: absolute;
    left: 0; right: 0;
    top: 352px;
    text-align: center;
    font-size: 18px;
    font-style: italic;
    letter-spacing: 7px;
    color: var(--back-text);
  }
</style>
</head>
<body>

<section class="card card-front" aria-label="Business card front">
  <div class="brand"><span class="brand-dot"></span>QUELVARIO</div>

  <h1 class="person-name">Marisolde Fuentes</h1>
  <p class="person-role">CEO/Founder</p>

  <ul class="contact-list">
    <li class="contact-item">
      <svg class="contact-icon" viewBox="0 0 24 24" aria-hidden="true"><path d="M6.6 10.8a15.1 15.1 0 0 0 6.6 6.6l2.2-2.2a1 1 0 0 1 1-.25 11.4 11.4 0 0 0 3.6.6 1 1 0 0 1 1 1V20a1 1 0 0 1-1 1A17 17 0 0 1 3 4a1 1 0 0 1 1-1h3.5a1 1 0 0 1 1 1c0 1.25.2 2.45.6 3.6a1 1 0 0 1-.25 1z"/></svg>
      787-555-0148
    </li>
    <li class="contact-item">
      <svg class="contact-icon" viewBox="0 0 24 24" aria-hidden="true"><path d="M2 5h20v2l-10 7L2 7z"/><path d="M2 9l10 7 10-7v10H2z"/></svg>
      ofuentes@kestrakom.example
    </li>
    <li class="contact-item">
      <svg class="contact-icon" viewBox="0 0 24 24" aria-hidden="true"><circle cx="12" cy="12" r="10"/><path d="M2 12h20M12 2c3 3 3 17 0 20M12 2c-3 3-3 17 0 20" fill="none" stroke="#f4f4f2" stroke-width="1.5"/></svg>
      www.kestrakom.example
    </li>
  </ul>

  <address class="location">
    Puerto Rico<br>latin caribbean island
  </address>

  <div class="front-trim"><span class="trim-line"></span><span class="trim-band"></span></div>
</section>

<section class="card card-back" aria-label="Business card back">
  <div class="brand"><span class="brand-dot"></span>QUELVARIO</div>
  <p class="back-url">www.kestrakom.example</p>
</section>

</body>
</html>
```